Business Card

Can you please copy the format provided for the business cards.
Can the logo be in the colours of the last file as specified.

Can the text please be in grey

• Navy Blue: #00457C
• Grey Text: #555555
• Orange Text: #FDBF29

The names on the business card will be

Dorian Pike
0455 718 302
dorian.pike@tallowridgeleasing.example.au

Lvl 7, 14 Harlow Pde
Merrivale QLD 4388
PO Box 3412
Sunhaven MC QLD 9812
P: 1300 742 619
F: 1300 742 638
www.tallowridgeleasing.example.au

And

Leon Whitcombe
0467 590 148
leon.whitcombe@tallowridgeleasing.example.au

Lvl 7, 14 Harlow Pde
Merrivale QLD 4388
PO Box 3412
Sunhaven MC QLD 9812
P: 1300 742 619
F: 1300 743 905

```html
<!DOCTYPE html>
<html lang="en">
<head>
<meta charset="utf-8">
<title>Tallow Ridge Leasing – Business Card</title>
<link rel="stylesheet" href="https://fonts.googleapis.com/css2?family=Ubuntu:wght@300;400;500;700&family=Ubuntu+Condensed&display=swap">
<style>
  :root {
    --navy: #00457C;
    --grey-text: #555555;
    --orange: #FDBF29;
    --stage: #e0e0e0;
    --card: #ffffff;
    --divider: #5a4a40;
  }
  * { margin: 0; padding: 0; box-sizing: border-box; }
  html, body {
    width: 1200px;
    height: 1016px;
    overflow: hidden;
    background: var(--stage);
    font-family: "Ubuntu", sans-serif;
  }
  .stage { position: relative; width: 1200px; height: 1016px; }
  .card {
    position: absolute;
    left: 279px;
    width: 641px;
    height: 365px;
    background: var(--card);
  }
  .card--front { top: 123px; }
  .card--back { top: 527px; }

  .brand {
    position: absolute;
    display: flex;
    align-items: center;
    gap: 14px;
  }
  .brand__square {
    width: 40px;
    height: 40px;
    background: var(--navy);
    flex: none;
  }
  .brand__name {
    font-family: "Ubuntu", sans-serif;
    font-weight: 700;
    color: var(--navy);
    font-size: 24px;
    letter-spacing: 0.5px;
    line-height: 1;
    white-space: nowrap;
  }
  .card--front .brand { left: 55px; top: 66px; }
  .card--back .brand { right: 315px; top: 166px; flex-direction: row-reverse; }
  .card--back .brand__name { font-size: 21px; }

  .holder {
    position: absolute;
    left: 55px;
    top: 256px;
    color: var(--grey-text);
  }
  .holder__name { font-size: 18px; font-weight: 400; line-height: 22px; letter-spacing: 0.3px; }
  .holder__mobile { font-size: 18px; font-weight: 500; line-height: 22px; letter-spacing: 0.5px; }
  .holder__email { font-size: 13px; font-weight: 400; margin-top: 6px; }

  .divider {
    position: absolute;
    left: 340px;
    top: 51px;
    width: 2px;
    height: 262px;
    background: var(--divider);
  }
  .contact {
    position: absolute;
    left: 371px;
    top: 101px;
    color: var(--grey-text);
    font-weight: 300;
    font-size: 16px;
    line-height: 20px;
  }
  .contact__group { margin-bottom: 6px; }
  .contact__web {
    font-family: "Ubuntu Condensed", sans-serif;
    font-size: 14px;
    font-weight: 400;
    margin-top: 4px;
  }
</style>
</head>
<body>
<main class="stage">
  <section class="card card--front">
    <div class="brand">
      <span class="brand__square"></span>
      <span class="brand__name">TALLOW RIDGE LEASING</span>
    </div>
    <div class="holder">
      <p class="holder__name">Dorian Pike</p>
      <p class="holder__mobile">0455 718 302</p>
      <p class="holder__email">dorian.pike@tallowridgeleasing.example.au</p>
    </div>
  </section>

  <section class="card card--back">
    <div class="brand">
      <span class="brand__square"></span>
      <span class="brand__name">TALLOW RIDGE LEASING</span>
    </div>
    <div class="divider"></div>
    <div class="contact">
      <p class="contact__group">Lvl 7, 14 Harlow Pde<br>Merrivale QLD 4388</p>
      <p class="contact__group">PO Box 3412<br>Sunhaven MC QLD 9812</p>
      <p class="contact__group">P: 1300 742 619<br>F: 1300 742 638</p>
      <p class="contact__web">www.tallowridgeleasing.example.au</p>
    </div>
  </section>
</main>
</body>
</html>
```